Brisk Lantern Accounting - New client package

I need a stationary package (presentation folder cover, welcome letter template/design, sample financial report template/design, business card and new logo) for my accounting business. I would like to see designs that use the color blue. Financial icons can be included in the design. The final design should be clean and communicate professionalism and the use of modern; user-friendly technology. Attached postcard files should help with overall design concept.

```html
<!DOCTYPE html>
<html lang="en">
<head>
<meta charset="utf-8">
<title>Brisk Lantern Accounting – Business Card</title>
<link href="https://fonts.googleapis.com/css2?family=Michroma&family=Saira+Semi+Condensed:wght@500&family=Roboto:wght@400&display=swap" rel="stylesheet">
<style>
  :root {
    --stage: #181818;
    --brand-blue: #2d5b8a;
    --brand-blue-soft: #3a6892;
    --card-white: #f9f9f9;
    --ink: #333333;
    --on-blue: #ffffff;
  }
  * { margin: 0; padding: 0; box-sizing: border-box; }
  html, body { width: 1200px; height: 1200px; overflow: hidden; }
  body { background: var(--stage); position: relative; }

  .card {
    position: absolute;
    left: 318px;
    width: 562px;
    height: 339px;
    overflow: hidden;
  }
  .card--front { top: 251px; background: var(--brand-blue); }
  .card--back { top: 609px; background: var(--card-white); }

  .front__disc {
    position: absolute;
    left: 106px; top: -3px;
    width: 344px; height: 344px;
    border-radius: 50%;
    background: var(--brand-blue-soft);
  }
  .wordmark {
    position: absolute;
    font-family: "Michroma", sans-serif;
    font-weight: 400;
    text-align: center;
    line-height: 1;
  }
  .wordmark__name { display: block; white-space: nowrap; }
  .wordmark__sub { display: block; white-space: nowrap; }

  .front__wordmark {
    left: 0; right: 0; top: 134px;
    color: var(--on-blue);
  }
  .front__wordmark .wordmark__name { font-size: 29px; letter-spacing: 0.5px; }
  .front__wordmark .wordmark__sub { font-size: 18px; letter-spacing: 19px; margin-top: 12px; padding-left: 19px; }

  .back__disc {
    position: absolute;
    left: 94px; top: 87px;
    width: 112px; height: 112px;
    border-radius: 50%;
    background: var(--brand-blue);
  }
  .back__wordmark {
    left: 20px; width: 260px; top: 208px;
    color: var(--brand-blue);
  }
  .back__wordmark .wordmark__name { font-size: 15px; }
  .back__wordmark .wordmark__sub { font-size: 10px; letter-spacing: 9px; margin-top: 6px; padding-left: 9px; }

  .contact {
    position: absolute;
    left: 298px; top: 102px;
  }
  .contact__name {
    font-family: "Saira Semi Condensed", sans-serif;
    font-weight: 500;
    font-size: 24px;
    color: var(--brand-blue);
    line-height: 1.1;
  }
  .contact__role {
    font-family: "Roboto", sans-serif;
    font-size: 14px;
    color: var(--ink);
    margin-top: 4px;
  }
  .contact__list { list-style: none; margin-top: 24px; }
  .contact__item {
    display: flex; align-items: center;
    font-family: "Roboto", sans-serif;
    font-size: 14.5px;
    color: var(--ink);
    height: 21px;
  }
  .contact__icon { width: 13px; height: 13px; margin-right: 9px; fill: var(--brand-blue); }
</style>
</head>
<body>
  <section class="card card--front">
    <div class="front__disc"></div>
    <div class="wordmark front__wordmark">
      <span class="wordmark__name">BRISK LANTERN</span>
      <span class="wordmark__sub">ACCOUNTING</span>
    </div>
  </section>

  <section class="card card--back">
    <div class="back__disc"></div>
    <div class="wordmark back__wordmark">
      <span class="wordmark__name">BRISK LANTERN</span>
      <span class="wordmark__sub">ACCOUNTING</span>
    </div>

    <div class="contact">
      <div class="contact__name">Mara Ellison</div>
      <div class="contact__role">Managing Director</div>
      <ul class="contact__list">
        <li class="contact__item">
          <svg class="contact__icon" viewBox="0 0 16 16" aria-hidden="true"><path d="M1 5c2-3 12-3 14 0v2h-4V5.5H5V7H1z"/><path d="M3 8h10l1 6H2z"/></svg>
          1.800.555.0142
        </li>
        <li class="contact__item">
          <svg class="contact__icon" viewBox="0 0 16 16" aria-hidden="true"><path d="M1 3h14v10H1z M2.5 4.5v.3L8 9l5.5-4.2v-.3z M2.5 6.6v5h11v-5L8 10.8z" fill-rule="evenodd"/></svg>
          info@brisklantern.com
        </li>
        <li class="contact__item">
          <svg class="contact__icon" viewBox="0 0 16 16" aria-hidden="true"><circle cx="8" cy="8" r="7"/><path d="M1 8h14M8 1v14M3 4h10M3 12h10" stroke="#f9f9f9" stroke-width="1" fill="none"/></svg>
          www.brisklantern.com
        </li>
      </ul>
    </div>
  </section>
</body>
</html>
```